Label Design for 2x Chutney Products

We need a label design for 2x Chutney Products.
Zintara Chutney - Red Chili
Zintara Chutney - Green Chili & Coriander
See attached pictures. This is just sample pictures so you get an impression of the product and the colors. Both labels to have as title the generic name "Zintara Chutney" and then added either Red Chili or Green Chili & Coriander. The different terms needs to be good readable and can differ in font/color/size, or in the same style if this makes more sense from design point (as I am not a designer). The labels later on need to be editable in the way that the ingredient list, nutrition list, basis company and production information can be added. If this needs to be done directly and cannot be edited later on please let know. Editable design related the additional text also would be good as the additional information need to be added in different languages (Dutch. German and perhaps French). No clue how this is to be implemented but looking forward to receive some input/solutions on this.
I already had a project to create the company logo. I consider this logo to be used as the product logo and not the company logo. A different company logo later on can be designed from new. This logo is here attached. Either to work with this logo and use it as product logo (perhaps revise the colors) and add the product description or create a new logo for the product from scratch if you feel too. The logo itself should be easily readable for the product name/description and the colors appealing to such product and of course customers.
Please contact if any clarification needed. Thanks in advance for your efforts and ideas for this project.

Industry/Entity Type

Food

Other font styles liked:
• Asian Touch

Requirements
Nice to have
• If possible "simply" editable for text fields in order to add/revise the ingredient list, nutrition list, revise to different languages.

```html
<!DOCTYPE html>
<html lang="en">
<head>
<meta charset="utf-8">
<title>Zintara Chutney – Red Chili Label</title>
<link rel="stylesheet" href="https://fonts.googleapis.com/css2?family=Fredoka:wght@600;700&family=Signika:wght@600&display=swap">
<style>
  :root {
    --label-red: #ed1c24;
    --band-dark: #1c2118;
    --tab-white: #ffffff;
    --brand-green: #7ed321;
    --title-green: #8be02a;
    --title-yellow: #ffe600;
    --title-black: #111111;
    --outline-grey: #b9b9b9;
    --text-white: #ffffff;
    --chili-red: #d8161c;
    --chili-stone: #b9a9a4;
  }
  * { margin: 0; padding: 0; box-sizing: border-box; }
  html, body {
    width: 1200px; height: 480px; overflow: hidden;
    background: var(--label-red);
  }
  .label {
    position: relative; width: 1200px; height: 480px;
    background: var(--label-red); overflow: hidden;
    font-family: "Fredoka", "Arial Rounded MT Bold", sans-serif;
  }
  .band {
    position: absolute; left: 0; width: 100%; height: 19px;
    background: var(--band-dark);
  }
  .band--top { top: 0; }
  .band--bottom { bottom: 0; height: 20px; }

  .brand-tab {
    position: absolute; left: 557px; top: 19px;
    width: 86px; height: 135px;
    background: var(--tab-white);
    border-radius: 0 0 10px 10px;
    display: flex; flex-direction: column; align-items: center;
    padding-top: 20px; gap: 10px;
  }
  .brand-tab__dot {
    width: 52px; height: 52px; border-radius: 50%;
    background: var(--label-red);
  }
  .brand-tab__name {
    font-family: "Fredoka", sans-serif; font-weight: 600;
    font-size: 13px; line-height: 1.05; text-align: center;
    color: var(--title-black); letter-spacing: 0.3px;
  }

  .chili-heart {
    position: absolute; left: 148px; top: 196px;
    width: 290px; height: 254px; border-radius: 50%;
    background:
      radial-gradient(ellipse 40% 42% at 45% 45%, var(--chili-red) 0%, rgba(216,22,28,0.85) 55%, rgba(216,22,28,0) 100%),
      radial-gradient(ellipse 50% 50% at 50% 50%, var(--chili-stone) 0%, rgba(185,169,164,0.6) 60%, rgba(237,28,36,0) 100%);
  }

  .product-title {
    position: absolute; left: 360px; top: 150px;
    width: 480px; height: 260px; overflow: visible;
  }
  .product-title text {
    font-family: "Fredoka", "Arial Rounded MT Bold", sans-serif;
    font-weight: 700; paint-order: stroke fill; stroke-linejoin: round;
  }
  .product-title .title-brand__outer { fill: var(--title-green); stroke: var(--outline-grey); stroke-width: 14px; }
  .product-title .title-brand__inner { fill: var(--title-green); stroke: var(--tab-white); stroke-width: 7px; }
  .product-title .title-kind__outer { fill: var(--title-black); stroke: var(--outline-grey); stroke-width: 16px; }
  .product-title .title-kind__inner { fill: var(--title-black); stroke: var(--title-yellow); stroke-width: 9px; }

  .variant {
    position: absolute; left: 524px; top: 346px;
    font-family: "Signika", sans-serif; font-weight: 600;
    font-size: 42px; color: var(--text-white);
    transform: skewX(-8deg); letter-spacing: 0.5px;
  }
</style>
</head>
<body>
  <main class="label">
    <div class="band band--top"></div>

    <div class="brand-tab">
      <span class="brand-tab__dot"></span>
      <span class="brand-tab__name">VELORA<br>FOODS</span>
    </div>

    <div class="chili-heart" role="img" aria-label="Photo of red chili peppers arranged in a heart shape on stone"></div>

    <svg class="product-title" viewBox="0 0 480 260" aria-label="Zintara Chutney">
      <g transform="skewX(-8)">
        <text class="title-brand__outer" x="90" y="86" font-size="74">Zintara</text>
        <text class="title-brand__inner" x="90" y="86" font-size="74">Zintara</text>
        <text class="title-kind__outer" x="112" y="160" font-size="84">Chutney</text>
        <text class="title-kind__inner" x="112" y="160" font-size="84">Chutney</text>
      </g>
    </svg>

    <p class="variant">Red Chili</p>

    <div class="band band--bottom"></div>
  </main>
</body>
</html>
```